Amber Orchard Reverie Event Flyer - Fundraiser for a US Senate Candidate

Working on an event flyer for a fundraiser for a Concordant candidate for Senate in Tennessee. Hosting an event for him that's a Amber Orchard Reverie theme, and I need a cool flyer that fits the theme with event details.
Host names will be added to the flyer on an ongoing basis, so will need someone who can quickly add names to flyer as hosts commit. Would like to agree to a fee for all work up front.
I'm attaching a mockup of a flyer that my friend did, before he had to back out because of work commitments, as well as a couple of pieces of Amber Orchard Reverie art that I think are cool.
Concordant

```html
<!DOCTYPE html>
<html lang="en">
<head>
<meta charset="utf-8">
<title>An Amber Orchard's CNC Meeting Eve – Reception for Daniel Harlow</title>
<link rel="stylesheet" href="https://fonts.googleapis.com/css2?family=Playball&family=Felipa&family=Carlito:wght@400;700&display=swap">
<style>
  :root {
    --night: #080c12;
    --canopy: #10161c;
    --glow: #ece2c4;
    --amber: #c9a867;
    --bark: #2b3c63;
    --meadow: #1a1e22;
    --white: #ffffff;
    --teal: #1fb3b1;
    --teal-deep: #0f9aa0;
    --body: #f2f2f2;
  }
  html, body {
    margin: 0;
    padding: 0;
    width: 848px;
    height: 1200px;
    overflow: hidden;
    background: var(--night);
  }
  .flyer {
    position: relative;
    width: 848px;
    height: 1200px;
    overflow: hidden;
    color: var(--white);
    text-align: center;
  }
  .scene {
    position: absolute;
    inset: 0;
    background:
      radial-gradient(ellipse 230px 210px at 330px 560px, rgba(240,230,200,0.9), rgba(200,185,150,0.35) 50%, transparent 80%),
      radial-gradient(ellipse 480px 380px at 460px 450px, rgba(150,160,170,0.55), transparent 75%),
      radial-gradient(ellipse 620px 260px at 560px 90px, rgba(201,168,103,0.22), transparent 70%),
      linear-gradient(180deg, #0d1218 0%, #1c2530 18%, #3a4652 40%, #56606a 55%, #3b4248 68%, #23282c 78%, #111417 90%, #07090b 100%);
  }
  .scene-canopy {
    position: absolute;
    left: 0;
    top: 0;
    width: 848px;
    height: 360px;
    background: radial-gradient(ellipse 520px 300px at 200px 60px, rgba(8,12,16,0.85), transparent 75%);
  }
  .scene-tree {
    position: absolute;
    left: 0;
    top: 0;
    width: 150px;
    height: 1200px;
    background: linear-gradient(90deg, #1c2a4a 0%, var(--bark) 55%, rgba(30,40,60,0) 100%);
    -webkit-mask-image: linear-gradient(180deg, rgba(0,0,0,0.3) 0%, #000 30%, #000 70%, rgba(0,0,0,0) 100%);
    mask-image: linear-gradient(180deg, rgba(0,0,0,0.3) 0%, #000 30%, #000 70%, rgba(0,0,0,0) 100%);
    opacity: 0.85;
  }
  .scene-meadow {
    position: absolute;
    left: 0;
    top: 700px;
    width: 848px;
    height: 500px;
    background: linear-gradient(180deg, rgba(40,46,52,0) 0%, rgba(60,66,70,0.55) 22%, rgba(26,30,34,0.8) 55%, rgba(6,8,10,0.95) 100%);
  }
  .line {
    position: absolute;
    left: 0;
    right: 0;
    margin: 0;
    white-space: nowrap;
  }
  .invite {
    top: 32px;
    font-family: "Playball", cursive;
    font-size: 36px;
    letter-spacing: 1px;
    text-shadow: 0 2px 4px rgba(0,0,0,0.6);
  }
  .title {
    font-family: "Playball", cursive;
    line-height: 1;
    font-weight: 400;
    -webkit-text-stroke: 2px currentColor;
    text-shadow: 0 3px 8px rgba(0,0,0,0.5);
  }
  .title-a { top: 66px; font-size: 150px; }
  .title-main { top: 186px; font-size: 108px; }
  .title-org {
    top: 294px;
    font-size: 104px;
    color: var(--teal);
  }
  .title-eve {
    top: 392px;
    font-size: 116px;
    color: var(--teal);
  }
  .detail {
    font-family: "Felipa", cursive;
    font-size: 32px;
    letter-spacing: 1px;
    text-shadow: 0 2px 5px rgba(0,0,0,0.85);
  }
  .detail sup { font-size: 0.55em; }
  .d1 { top: 582px; }
  .d2 { top: 624px; }
  .d3 { top: 714px; }
  .d4 { top: 768px; font-size: 35px; }
  .info {
    font-family: "Carlito", sans-serif;
    font-size: 20px;
    color: var(--body);
  }
  .i1 { top: 862px; }
  .i2 { top: 898px; }
  .i3 { top: 954px; }
  .i4 { top: 982px; }
  .or {
    position: absolute;
    left: 640px;
    top: 966px;
    font-family: "Felipa", cursive;
    font-size: 24px;
  }
  .paid {
    top: 1070px;
    font-family: "Carlito", sans-serif;
    font-size: 19px;
    font-variant: small-caps;
    letter-spacing: 2px;
  }
  .brand {
    position: absolute;
    left: 0;
    right: 0;
    top: 1118px;
    display: flex;
    justify-content: center;
    align-items: center;
    gap: 10px;
    font-family: "Carlito", sans-serif;
    font-weight: 700;
    font-size: 26px;
    letter-spacing: 1px;
    color: var(--white);
  }
  .brand-mark {
    width: 14px;
    height: 14px;
    border-radius: 50%;
    background: var(--white);
  }
</style>
</head>
<body>
  <main class="flyer">
    <div class="scene" role="img" aria-label="Moonlit amber orchard at night with a glowing sky beyond the trees and sparkling stars in the branches"></div>
    <div class="scene-canopy" role="img" aria-label="Dark leafy orchard canopy across the top"></div>
    <div class="scene-tree" role="img" aria-label="Tree trunk at the left edge"></div>
    <div class="scene-meadow" role="img" aria-label="Misty meadow and distant hills fading into night"></div>

    <p class="line invite">You're Cordially Invited to</p>
    <h1 class="line title title-a">An</h1>
    <p class="line title title-main">Amber Orchard's</p>
    <p class="line title title-org">CNC</p>
    <p class="line title title-eve">Meeting Eve</p>

    <p class="line detail d1">Reception for Daniel Harlow</p>
    <p class="line detail d2">Wednesday, August 23<sup>rd</sup> 6<sup>00</sup>-9<sup>00</sup>pm</p>
    <p class="line detail d3">House of Owen Pritchard</p>
    <p class="line detail d4">418B Linden Row, Nashville, TN 37219</p>

    <p class="line info i1">Suggested Contribution:</p>
    <p class="line info i2">$20.18 Friend | $100 Supporter | $250 Host</p>
    <p class="line info i3">RSVP at www.DanielHarlow.com/Orchard</p>
    <p class="line info i4">RSVP by Email at RSVP@DanielHarlow.com</p>
    <span class="or">or</span>

    <p class="line paid">Paid for by Harlow for U.S. Senate</p>
    <div class="brand"><span class="brand-mark"></span><span>DANIEL HARLOW</span></div>
  </main>
</body>
</html>
```